New Web Design Project

See attachments on the content and concept. Very important that the flow of the tiers stand out

Target Market(s)

Food and Beverage Manufacturing

Industry/Entity Type

Food and Beverage

Coding

Coded - Design and coding required

Number of Pages Required

3 page

Colors
0054AA
0677BA
7BADD7
CADEEF
E8F1F8

```html
<!DOCTYPE html>
<html lang="en">
<head>
<meta charset="utf-8">
<title>Keystone Compliance Group — SQF Consulting</title>
<link href="https://fonts.googleapis.com/css2?family=Playfair+Display:wght@600;700&family=Poppins:wght@400;500;600;700&display=swap" rel="stylesheet">
<style>
:root{
  --navy:#13285E;
  --navy-deep:#0E1F4C;
  --blue:#0054AA;
  --blue-2:#0677BA;
  --sky:#7BADD7;
  --mist:#CADEEF;
  --ice:#E8F1F8;
  --ink:#1C2445;
  --muted:#4A5370;
  --green:#5AA23A;
  --white:#FFFFFF;
  --serif:'Playfair Display', Georgia, serif;
  --sans:'Poppins', Arial, sans-serif;
}
*{box-sizing:border-box;margin:0;padding:0}
html,body{width:1200px;height:4065px;overflow:hidden}
body{font-family:var(--sans);color:var(--ink);background:var(--white)}
.page{position:relative;width:1200px;height:4065px;overflow:hidden;background:var(--white)}
.abs{position:absolute}
.serif{font-family:var(--serif);text-transform:uppercase;color:var(--navy);font-weight:700}
.eyebrow{font-size:9px;font-weight:600;letter-spacing:.4px;text-transform:uppercase;color:var(--navy)}
.center{text-align:center;left:0;width:1200px}
.btn{position:absolute;display:flex;align-items:center;justify-content:center;font-size:9.5px;font-weight:700;text-transform:uppercase;border-radius:6px;letter-spacing:.2px}
.btn-primary{background:var(--blue);color:var(--white)}
.btn-ghost{border:1.5px solid var(--navy);color:var(--navy)}
.btn-outline-light{border:1.5px solid var(--white);color:var(--white)}

/* header */
.site-header{position:absolute;top:0;left:0;width:1200px;height:74px;background:var(--white);z-index:5}
.brand{position:absolute;left:131px;top:16px;display:flex;align-items:center;gap:8px}
.brand-mark{width:34px;height:34px;border-radius:50%;border:3px solid var(--blue)}
.brand-name{font-family:var(--serif);font-weight:700;font-size:19px;color:var(--navy);line-height:1}
.brand-sub{font-size:8.5px;letter-spacing:.6px;color:var(--navy);text-transform:uppercase;margin-top:3px}
.nav a{position:absolute;top:30px;font-size:9.5px;color:var(--ink);text-decoration:none;text-transform:uppercase}

/* hero */
.hero-photo{left:0;top:74px;width:1200px;height:830px;background:linear-gradient(100deg,#f1f4f7 0%,#e3e9ef 40%,#cfd8e1 62%,#aab8c6 80%,#c3ccd6 100%)}
.hero-title{left:131px;top:244px;font-size:34px;line-height:38px;letter-spacing:.3px}
.hero-copy{left:131px;top:372px;width:430px;font-size:11px;line-height:14.5px;color:var(--ink)}
.scroll-cue{left:131px;top:576px;width:30px;height:50px;border:1.5px solid var(--navy);border-radius:15px;display:flex;align-items:center;justify-content:center;color:var(--navy);font-size:16px}
.stat{position:absolute;top:836px;width:170px;text-align:center;color:var(--white)}
.stat-num{font-family:var(--serif);font-weight:700;font-size:32px;line-height:36px}
.stat-label{font-size:10.5px;margin-top:4px}
.stat-div{position:absolute;top:820px;width:1px;height:90px;background:rgba(255,255,255,.35)}

/* services */
.section-title{font-size:30px;line-height:35px}
.section-copy{font-size:10.5px;line-height:15px;color:var(--muted)}
.svc-card{position:absolute;top:1276px;width:270px;height:197px;background:var(--white);border-radius:14px;box-shadow:0 6px 22px rgba(19,40,94,.07)}
.svc-badge{position:absolute;top:-41px;left:33px;width:72px;height:80px}
.svc-title{position:absolute;left:32px;top:62px;font-family:var(--serif);font-weight:700;font-size:14px;color:var(--navy);text-transform:uppercase;white-space:nowrap}
.svc-text{position:absolute;left:32px;top:90px;width:215px;font-size:9.8px;line-height:13.5px;color:var(--muted)}
.dot{position:absolute;top:1518px;width:8px;height:8px;border-radius:50%}

/* why */
.benefit{position:absolute;left:183px;width:440px}
.benefit-tick{position:absolute;left:0;top:1px;width:15px;height:15px}
.benefit-title{margin-left:25px;font-family:var(--serif);font-weight:700;font-size:14px;color:var(--navy);text-transform:uppercase}
.benefit-text{margin-left:25px;margin-top:3px;font-size:9.8px;line-height:13.5px;color:var(--muted)}

/* process */
.tier{position:absolute;top:2526px;width:226px;height:266px}
.tier svg{position:absolute;left:0;top:0}
.tier-body{position:absolute;left:0;top:0;width:226px;height:266px;text-align:center;color:var(--white)}
.tier-icon{position:absolute;left:90px;top:52px;width:46px;height:46px}
.tier-title{position:absolute;top:122px;left:0;width:226px;font-family:var(--serif);font-weight:700;font-size:14px;text-transform:uppercase}
.tier-text{position:absolute;top:148px;left:38px;width:150px;font-size:9.8px;line-height:13.2px}

/* testimonial */
.laurel{top:3045px;width:64px;height:124px;background:linear-gradient(180deg,var(--navy),var(--blue));border-radius:40px 40px 30px 30px;opacity:.9}
.quote{left:330px;top:3053px;width:540px;font-size:18.5px;line-height:25.3px;text-align:center}

.cred{position:absolute;top:3261px;width:224px;height:76px;border:1.5px solid var(--navy);border-radius:22px}
.cred svg{position:absolute;left:28px;top:19px}
.cred-label{position:absolute;left:86px;top:20px;font-family:var(--serif);font-weight:700;font-size:13px;line-height:16px;color:var(--navy);text-transform:uppercase}

/* cta + footer */
.cta-title{left:230px;top:3562px;font-size:30px;color:var(--white)}
.cta-copy{left:230px;top:3606px;width:440px;font-size:10px;line-height:15.5px;color:var(--white)}
.foot-head{position:absolute;top:3775px;font-family:var(--serif);font-weight:700;font-size:17px;color:var(--white);text-transform:uppercase}
.foot-list{position:absolute;left:508px;top:3812px;list-style:none}
.foot-list li{font-size:10px;color:var(--mist);line-height:19px;display:flex;align-items:center;gap:8px}
.contact{position:absolute;left:703px;width:190px}
.contact-label{font-size:10px;font-weight:600;color:var(--white);text-transform:uppercase;margin-left:18px;position:relative}
.contact-label svg{position:absolute;left:-18px;top:2px}
.contact-val{font-size:9.5px;line-height:15.5px;color:var(--mist);margin-left:18px}
.social{position:absolute;width:28px;height:28px;border-radius:50%;background:rgba(255,255,255,.12);border:1px solid rgba(255,255,255,.25)}
.social span{position:absolute;left:9px;top:9px;width:10px;height:10px;border-radius:50%;background:var(--white)}
.copyright{left:0;top:4018px;width:1200px;height:47px;background:var(--navy-deep);color:var(--mist);font-size:9.5px;display:flex;align-items:center;justify-content:center}
.chat{left:1112px;top:3996px;width:44px;height:44px;border-radius:50%;background:var(--blue);display:flex;align-items:center;justify-content:center}
</style>
</head>
<body>
<div class="page">

  <!-- header -->
  <header class="site-header">
    <div class="brand">
      <div class="brand-mark"></div>
      <div>
        <div class="brand-name">Keystone Compliance Group</div>
        <div class="brand-sub">Food Safety &amp; SQF Certification</div>
      </div>
    </div>
    <nav class="nav">
      <a style="left:582px">Services</a>
      <a style="left:653px">Benefits</a>
      <a style="left:720px">Process</a>
      <a style="left:790px">Contact</a>
    </nav>
    <svg class="abs" style="left:853px;top:27px" width="18" height="18" viewBox="0 0 24 24" fill="none" stroke="#13285E" stroke-width="2"><path d="M20 14.5A8 8 0 0 1 9.5 4a8 8 0 1 0 10.5 10.5z"/></svg>
    <div class="btn btn-primary" style="left:897px;top:17px;width:172px;height:38px">Get SQF Consultation</div>
  </header>

  <!-- hero -->
  <div class="abs hero-photo" role="img" aria-label="Food safety specialist reviewing a compliance checklist on a tablet in a bright production facility"></div>
  <svg class="abs" style="left:0;top:600px" width="1200" height="420" viewBox="0 0 1200 420">
    <polygon points="0,24 600,200 1200,24 1200,300 600,414 0,300" fill="#0054AA"/>
    <polygon points="0,24 600,200 1200,24 1200,60 600,230 0,60" fill="#0677BA" opacity=".35"/>
  </svg>
  <div class="abs eyebrow" style="left:131px;top:223px">SQF Only · Tech Driven</div>
  <h1 class="abs serif hero-title">Hire a Tech-Driven SQF Team<br>That Carries You Across the<br>Certification Finish Line.</h1>
  <p class="abs hero-copy">At Keystone Compliance Group, we focus exclusively on SQF — combining real plant experience with smart technology so your team can stay focused on production while we handle the path to certification and beyond.</p>
  <div class="btn btn-primary" style="left:131px;top:437px;width:169px;height:38px">Get SQF Consultation</div>
  <div class="btn btn-ghost" style="left:309px;top:437px;width:127px;height:38px">Explore Services</div>
  <div class="abs scroll-cue">↓</div>

  <div class="stat" style="left:258px"><div class="stat-num">15+</div><div class="stat-label">Clients Onboarded</div></div>
  <div class="stat-div" style="left:425px"></div>
  <div class="stat" style="left:406px"><div class="stat-num">100%</div><div class="stat-label">SQF Focused</div></div>
  <div class="stat-div" style="left:558px"></div>
  <div class="stat" style="left:575px"><div class="stat-num">Digital</div><div class="stat-label">Platform Built Programs</div></div>
  <div class="stat-div" style="left:760px"></div>
  <div class="stat" style="left:763px"><div class="stat-num">US</div><div class="stat-label">Nationwide Coverage</div></div>

  <!-- services -->
  <svg class="abs" style="left:0;top:900px;z-index:0" width="1200" height="680" viewBox="0 0 1200 680">
    <polygon points="0,0 0,0 0,576 600,679 1200,576 1200,0" fill="#E8F1F8"/>
  </svg>
  <svg class="abs" style="left:0;top:600px" width="1200" height="420" viewBox="0 0 1200 420">
    <polygon points="0,300 600,414 1200,300 1200,300" fill="#0054AA"/>
    <polygon points="0,24 600,200 1200,24 1200,300 600,414 0,300" fill="#0054AA"/>
  </svg>
  <div class="abs eyebrow center" style="top:1076px">What We Do</div>
  <h2 class="abs serif section-title center" style="top:1092px">SQF Consulting, Implementation<br>&amp; Onboarding</h2>
  <p class="abs section-copy center" style="top:1173px">We help food and beverage manufacturers achieve and maintain SQF certification with confidence, using<br>practical programs and digital tools that work on the floor — not just on audit day.</p>

  <div class="svc-card" style="left:131px">
    <svg class="svc-badge" viewBox="0 0 72 80"><path d="M36 0 L72 16 L72 52 Q72 80 36 80 Q0 80 0 52 L0 16Z" fill="#13285E"/><circle cx="36" cy="40" r="12" fill="none" stroke="#fff" stroke-width="2"/><circle cx="36" cy="40" r="4" fill="none" stroke="#fff" stroke-width="2"/></svg>
    <div class="svc-title">SQF Program Design</div>
    <p class="svc-text">We design your complete SQF system from scratch — HACCP/food safety plans, prerequisite programs, SOPs, forms, logs, and all required documentation tailored to your facility.</p>
  </div>
  <div class="svc-card" style="left:417px">
    <svg class="svc-badge" viewBox="0 0 72 80"><path d="M36 0 L72 16 L72 52 Q72 80 36 80 Q0 80 0 52 L0 16Z" fill="#0054AA"/><rect x="24" y="30" width="24" height="16" rx="2" fill="none" stroke="#fff" stroke-width="2"/><line x1="20" y1="50" x2="52" y2="50" stroke="#fff" stroke-width="2"/></svg>
    <div class="svc-title">Digital Platform Build</div>
    <p class="svc-text">We build your SQF program directly into modern food safety software like BatchLedger or LineSafe — digitizing forms, checklists, monitoring logs, and workflows so your team runs paperless.</p>
  </div>
  <div class="svc-card" style="left:704px">
    <svg class="svc-badge" viewBox="0 0 72 80"><path d="M36 0 L72 16 L72 52 Q72 80 36 80 Q0 80 0 52 L0 16Z" fill="#13285E"/><circle cx="30" cy="33" r="5" fill="none" stroke="#fff" stroke-width="2"/><path d="M22 52 Q22 42 30 42 Q38 42 38 52" fill="none" stroke="#fff" stroke-width="2"/><rect x="40" y="28" width="12" height="10" fill="none" stroke="#fff" stroke-width="2"/></svg>
    <div class="svc-title">Coaching &amp; Support</div>
    <p class="svc-text">After building your system, we coach your team to own and maintain it day-to-day. You run the program; we provide ongoing expert guidance so you stay audit-ready at all times.</p>
  </div>
  <div class="svc-card" style="left:990px">
    <svg class="svc-badge" viewBox="0 0 72 80"><path d="M36 0 L72 16 L72 52 Q72 80 36 80 Q0 80 0 52 L0 16Z" fill="#13285E"/><rect x="24" y="27" width="18" height="24" fill="none" stroke="#fff" stroke-width="2"/><circle cx="44" cy="46" r="5" fill="none" stroke="#fff" stroke-width="2"/><line x1="48" y1="50" x2="52" y2="54" stroke="#fff" stroke-width="2"/></svg>
    <div class="svc-title">Gap Assessments</div>
    <p class="svc-text">We evaluate where your facility stands against SQF requirements, identify gaps, and provide a clear roadmap to close them before your audit — no surprises on certification day.</p>
  </div>
  <div class="dot" style="left:588px;background:var(--navy)"></div>
  <div class="dot" style="left:602px;background:var(--mist)"></div>

  <!-- why -->
  <div class="abs eyebrow center" style="top:1664px">Why Keystone Compliance</div>
  <h2 class="abs serif section-title center" style="top:1683px;line-height:31px">Built for Small &amp; Mid Size<br>Manufacturers</h2>
  <p class="abs section-copy center" style="top:1754px">You don't need to hire a full-time food safety director or figure out SQF alone. We bring the<br>expertise and technology you stay focused on production.</p>

  <div class="benefit" style="top:1852px">
    <svg class="benefit-tick" viewBox="0 0 16 16"><circle cx="8" cy="8" r="8" fill="#5AA23A"/><path d="M4.5 8.2 L7 10.5 L11.5 5.8" fill="none" stroke="#fff" stroke-width="1.8"/></svg>
    <div class="benefit-title">Lower Cost Than a Full-Time Hire</div>
    <p class="benefit-text">Get a complete SQF team — program design, digital implementation, and<br>coaching — at a fraction of the cost of hiring a full-time SQF Practitioner.</p>
  </div>
  <div class="benefit" style="top:1930px">
    <svg class="benefit-tick" viewBox="0 0 16 16"><circle cx="8" cy="8" r="8" fill="#5AA23A"/><path d="M4.5 8.2 L7 10.5 L11.5 5.8" fill="none" stroke="#fff" stroke-width="1.8"/></svg>
    <div class="benefit-title">Your Program Lives in Software</div>
    <p class="benefit-text">No more binders and spreadsheets. Your SQF system is built into BatchLedger<br>or LineSafe — organized, accessible, and always audit-ready.</p>
  </div>
  <div class="benefit" style="top:2008px">
    <svg class="benefit-tick" viewBox="0 0 16 16"><circle cx="8" cy="8" r="8" fill="#5AA23A"/><path d="M4.5 8.2 L7 10.5 L11.5 5.8" fill="none" stroke="#fff" stroke-width="1.8"/></svg>
    <div class="benefit-title">You Own It, We Support It</div>
    <p class="benefit-text">We build the system and train your team. You maintain and run it day-to-day.<br>We stay on call with coaching and advisory so you never feel stuck.</p>
  </div>
  <div class="benefit" style="top:2080px">
    <svg class="benefit-tick" viewBox="0 0 16 16"><circle cx="8" cy="8" r="8" fill="#5AA23A"/><path d="M4.5 8.2 L7 10.5 L11.5 5.8" fill="none" stroke="#fff" stroke-width="1.8"/></svg>
    <div class="benefit-title">Flexible, Low-Risk Engagement</div>
    <p class="benefit-text">Start with a 3-month commitment, then go month-to-month. Cancel anytime<br>with 30 days notice. We earn your business every month.</p>
  </div>
  <div class="benefit" style="top:2159px">
    <svg class="benefit-tick" viewBox="0 0 16 16"><circle cx="8" cy="8" r="8" fill="#5AA23A"/><path d="M4.5 8.2 L7 10.5 L11.5 5.8" fill="none" stroke="#fff" stroke-width="1.8"/></svg>
    <div class="benefit-title">Bilingual Floor-Level Support</div>
    <p class="benefit-text">With our Central America team, we provide training and documentation in Spanish<br>so every member of your production team understands and follows the program.</p>
  </div>

  <svg class="abs" style="left:644px;top:1813px" width="376" height="432" viewBox="0 0 376 432">
    <path d="M188 0 L376 94 L376 290 Q376 432 188 432 Q0 432 0 290 L0 94 Z" fill="#0054AA"/>
    <path d="M188 20 L356 104 L356 290 Q356 412 188 412 Q20 412 20 290 L20 104 Z" fill="#fff"/>
    <defs><linearGradient id="labTone" x1="0" y1="0" x2="1" y2="1"><stop offset="0" stop-color="#e4e9ee"/><stop offset=".55" stop-color="#b9c4cf"/><stop offset="1" stop-color="#7d8c9c"/></linearGradient></defs>
    <path role="img" aria-label="Lab technician in protective gear using a microscope in a food testing lab" d="M188 44 L332 116 L332 290 Q332 388 188 388 Q44 388 44 290 L44 116 Z" fill="url(#labTone)"/>
  </svg>

  <!-- process -->
  <svg class="abs" style="left:0;top:2324px" width="1200" height="640" viewBox="0 0 1200 640">
    <polygon points="0,0 1200,0 1200,471 600,637 0,471" fill="#E8F1F8"/>
  </svg>
  <div class="abs eyebrow center" style="top:2416px">How It Works</div>
  <h2 class="abs serif section-title center" style="top:2437px">From Discovery to Certification</h2>
  <p class="abs section-copy center" style="top:2482px">A clear, structured path that takes the guesswork out of SQF.</p>

  <div class="tier" style="left:131px">
    <svg width="226" height="266" viewBox="0 0 226 266"><path d="M113 0 L226 54 L226 153 A113 113 0 0 1 0 153 L0 54 Z" fill="#13285E"/></svg>
    <div class="tier-body">
      <svg class="tier-icon" viewBox="0 0 46 46" fill="none" stroke="#fff" stroke-width="1.8"><path d="M8 18 Q23 6 38 18 L34 22 L28 19 L28 15 Q23 13 18 15 L18 19 L12 22 Z"/><rect x="12" y="24" width="22" height="14" rx="3"/><circle cx="23" cy="31" r="3"/></svg>
      <div class="tier-title">Discovery Call</div>
      <p class="tier-text">We learn about your facility, your current systems, and where you are in the SQF journey. No pressure — just a conversation.</p>
    </div>
  </div>
  <div class="tier" style="left:368px">
    <svg width="226" height="266" viewBox="0 0 226 266"><path d="M113 0 L226 54 L226 153 A113 113 0 0 1 0 153 L0 54 Z" fill="#0054AA"/></svg>
    <div class="tier-body">
      <svg class="tier-icon" viewBox="0 0 46 46" fill="none" stroke="#fff" stroke-width="1.8"><rect x="10" y="8" width="22" height="30" rx="2"/><circle cx="25" cy="26" r="7"/><line x1="30" y1="31" x2="37" y2="38"/><line x1="14" y1="14" x2="26" y2="14"/></svg>
      <div class="tier-title">Gap Assessment</div>
      <p class="tier-text">We evaluate your facility against SQF requirements, identify what's missing, and give you a clear roadmap with priorities.</p>
    </div>
  </div>
  <div class="tier" style="left:605px">
    <svg width="226" height="266" viewBox="0 0 226 266"><path d="M113 0 L226 54 L226 153 A113 113 0 0 1 0 153 L0 54 Z" fill="#0677BA"/></svg>
    <div class="tier-body">
      <svg class="tier-icon" viewBox="0 0 46 46" fill="none" stroke="#fff" stroke-width="1.8"><rect x="8" y="26" width="10" height="10"/><rect x="18" y="16" width="10" height="10"/><rect x="28" y="6" width="10" height="10"/><line x1="8" y1="40" x2="38" y2="40"/></svg>
      <div class="tier-title">Build &amp; Implement</div>
      <p class="tier-text">We design your SQF program and build it directly into your digital food safety platform — forms, logs, SOPs, HACCP plans, all of it.</p>
    </div>
  </div>
  <div class="tier" style="left:842px">
    <svg width="226" height="266" viewBox="0 0 226 266"><path d="M113 0 L226 54 L226 153 A113 113 0 0 1 0 153 L0 54 Z" fill="#7BADD7"/></svg>
    <div class="tier-body">
      <svg class="tier-icon" viewBox="0 0 46 46" fill="none" stroke="#fff" stroke-width="1.8"><circle cx="12" cy="22" r="4"/><path d="M6 38 L6 30 Q12 26 18 30 L18 38"/><path d="M20 32 L28 24 L33 28 L40 14"/><polyline points="35,14 40,14 40,19"/></svg>
      <div class="tier-title">Coach &amp; Certify</div>
      <p class="tier-text">We train your team, run mock audits, and prepare you for certification day. Then we stay on as your ongoing SQF advisory partner.</p>
    </div>
  </div>

  <!-- testimonial -->
  <div class="abs laurel" style="left:262px" role="img" aria-label="Laurel wreath ornament, left half"></div>
  <div class="abs laurel" style="left:874px" role="img" aria-label="Laurel wreath ornament, right half"></div>
  <blockquote class="abs serif quote">Keystone Compliance Group didn't just hand us a binder. They built our entire SQF system into software and coached our team until we owned it. We passed our first audit with confidence.</blockquote>
  <div class="abs eyebrow center" style="top:3186px;font-size:9.5px">— SQF-Certified Manufacturing Client</div>

  <div class="cred" style="left:131px">
    <svg width="40" height="38" viewBox="0 0 40 38" fill="none" stroke="#13285E" stroke-width="1.8"><circle cx="14" cy="10" r="6"/><path d="M4 36 L4 26 Q14 18 24 26 L24 36"/><rect x="26" y="6" width="12" height="16" rx="1"/></svg>
    <div class="cred-label">SQF<br>Practitioner</div>
  </div>
  <div class="cred" style="left:369px">
    <svg width="40" height="38" viewBox="0 0 40 38" fill="none" stroke="#13285E" stroke-width="1.8"><ellipse cx="20" cy="14" rx="17" ry="7"/><path d="M14 18 L8 32 M26 18 L32 32"/><rect x="16" y="10" width="8" height="8"/></svg>
    <div class="cred-label">Six Sigma<br>Black Belt</div>
  </div>
  <div class="cred" style="left:608px">
    <svg width="40" height="38" viewBox="0 0 40 38" fill="none" stroke="#13285E" stroke-width="1.8"><rect x="6" y="12" width="26" height="14" rx="4" transform="rotate(-35 19 19)"/><circle cx="15" cy="22" r="2"/><path d="M30 4 Q36 6 37 12 M28 8 Q32 9 33 13"/></svg>
    <div class="cred-label">Remote &amp;<br>On-Site</div>
  </div>
  <div class="cred" style="left:846px">
    <svg width="40" height="38" viewBox="0 0 40 38" fill="none" stroke="#13285E" stroke-width="1.8"><circle cx="20" cy="16" r="7"/><path d="M17 24 L17 30 L23 30 L23 24"/><path d="M20 2 L20 5 M6 16 L9 16 M31 16 L34 16 M10 6 L12 8 M30 6 L28 8"/></svg>
    <div class="cred-label">Digital<br>First</div>
  </div>

  <!-- cta + footer -->
  <svg class="abs" style="left:0;top:3418px" width="1200" height="647" viewBox="0 0 1200 647">
    <polygon points="0,119 600,0 1200,119 1200,647 0,647" fill="#13285E"/>
  </svg>
  <h2 class="abs serif cta-title">Ready to Talk SQF?</h2>
  <p class="abs cta-copy">Share a few details about your facility and where you are in the SQF journey. We'll follow up with a brief discovery call and a clear next step.</p>
  <div class="btn btn-primary" style="left:733px;top:3570px;width:235px;height:36px">Get My SQF Consultation</div>
  <div class="btn btn-outline-light" style="left:733px;top:3616px;width:235px;height:38px">Visit PlantwiseOps.com</div>
  <div class="abs" style="left:131px;top:3698px;width:938px;height:1px;background:rgba(255,255,255,.2)"></div>

  <div class="abs" style="left:186px;top:3802px;display:flex;align-items:center;gap:8px">
    <div style="width:34px;height:34px;border-radius:50%;border:3px solid var(--blue-2)"></div>
    <div>
      <div style="font-family:var(--serif);font-weight:700;font-size:18px;color:#fff;line-height:1">Keystone Compliance Group</div>
      <div style="font-size:8.5px;letter-spacing:.6px;color:#fff;text-transform:uppercase;margin-top:3px">Food Safety &amp; SQF Certification</div>
    </div>
  </div>
  <p class="abs" style="left:186px;top:3856px;width:285px;font-size:9.5px;line-height:15.5px;color:var(--mist)">Tech-driven SQF consulting for small and mid-size US food manufacturers. Based in Modesto, CA — serving clients across North America.</p>

  <div class="foot-head" style="left:508px">Services</div>
  <ul class="foot-list">
    <li><svg width="9" height="9" viewBox="0 0 10 10"><path d="M1 5 L4 8 L9 2" fill="none" stroke="#fff" stroke-width="1.6"/></svg>SQF Program Design</li>
    <li><svg width="9" height="9" viewBox="0 0 10 10"><path d="M1 5 L4 8 L9 2" fill="none" stroke="#fff" stroke-width="1.6"/></svg>Digital Platform Build</li>
    <li><svg width="9" height="9" viewBox="0 0 10 10"><path d="M1 5 L4 8 L9 2" fill="none" stroke="#fff" stroke-width="1.6"/></svg>Coaching &amp; Support</li>
    <li><svg width="9" height="9" viewBox="0 0 10 10"><path d="M1 5 L4 8 L9 2" fill="none" stroke="#fff" stroke-width="1.6"/></svg>Gap Assessments</li>
    <li><svg width="9" height="9" viewBox="0 0 10 10"><path d="M1 5 L4 8 L9 2" fill="none" stroke="#fff" stroke-width="1.6"/></svg>Sanitation Programs</li>
  </ul>

  <div class="foot-head" style="left:703px">Connect</div>
  <div class="contact" style="top:3815px">
    <div class="contact-label"><svg width="11" height="9" viewBox="0 0 11 9"><rect width="11" height="9" rx="1" fill="#fff"/><path d="M0.5 1 L5.5 5 L10.5 1" fill="none" stroke="#13285E" stroke-width="1"/></svg>Email Us</div>
    <div class="contact-val">hello@plantwiseops.com</div>
  </div>
  <div class="contact" style="top:3855px">
    <div class="contact-label"><svg width="11" height="11" viewBox="0 0 24 24"><path d="M6 2 L10 2 L11 7 L8 9 Q10 14 15 16 L17 13 L22 14 L22 18 Q22 22 18 22 Q3 20 2 6 Q2 2 6 2Z" fill="#fff"/></svg>Phone</div>
    <div class="contact-val">(555) 014-2290</div>
  </div>
  <div class="contact" style="top:3895px">
    <div class="contact-label"><svg width="9" height="12" viewBox="0 0 10 14"><path d="M5 0 Q10 0 10 5 Q10 8 5 14 Q0 8 0 5 Q0 0 5 0Z" fill="#fff"/><circle cx="5" cy="5" r="2" fill="#13285E"/></svg>Email Address</div>
    <div class="contact-val">Sample note about our studio,<br>giving a short line on its roots.</div>
  </div>

  <div class="foot-head" style="left:919px">Follow Me</div>
  <div class="social" style="left:921px;top:3821px"><span></span></div>
  <div class="social" style="left:956px;top:3821px"><span></span></div>
  <div class="social" style="left:989px;top:3821px"><span></span></div>
  <div class="social" style="left:921px;top:3856px"><span></span></div>
  <div class="social" style="left:956px;top:3856px"><span></span></div>

  <div class="abs copyright">© 2026 Keystone Compliance Group LLC. All rights reserved. Created with Lumen Studio</div>
  <div class="abs chat"><svg width="22" height="20" viewBox="0 0 22 20"><path d="M11 1 Q21 1 21 9 Q21 16 11 16 L5 19 L6 15 Q1 13 1 9 Q1 1 11 1Z" fill="#fff"/><circle cx="7" cy="9" r="1.4" fill="#0054AA"/><circle cx="11" cy="9" r="1.4" fill="#0054AA"/><circle cx="15" cy="9" r="1.4" fill="#0054AA"/></svg></div>

</div>
</body>
</html>
```